Moder Business Card Design for Renewables Business

Need a business card design for my business. We collect & repurpose spent coffee ground from cafes. The cards will be made from recycled paper. Needs to fit our corporate colour scheme of white, green & brown (see logo for colour codes). Eco friendly, modern, intresting & eye catching.
This card needs to convey the message of the business and fit into its mantra of eco-friendly, sustainable etc.

Target Market(s)

Cafe Owners, Coffee Drinkers, Recycling Companies, Farmers

Industry/Entity Type

Recycling

Contact Information for Business Card

Name; Peter Dalton
Phone; 0438 216 570
e-mail; info@florivex.com.au
website; www.florivex.com.au

Font styles to use
Sans Serif
Script

Colors

Designer to choose colors to be used in the design.

Requirements
Must have
• FRONT;
• Logo, Name (Peter Dalton), phone number, e-mail address, website
• BACK;
• On the back in cursive text; 'RENEWAL IN EVERY SINGLE CUP'
• Small facebook & Instagram logos with text 'Florivex'
Should not have
• messy design

```html
<!DOCTYPE html>
<html lang="en">
<head>
<meta charset="utf-8">
<title>Florivex Business Cards</title>
<link href="https://fonts.googleapis.com/css2?family=Open+Sans:wght@400;600&display=swap" rel="stylesheet">
<style>
  :root {
    --canvas-bg: #161616;
    --card-top: #1f1f1f;
    --card-bottom: #121212;
    --deco-tone: #262626;
    --brand-green: #7dbb3c;
    --brand-brown: #8a4a1f;
    --text-light: #e8e8e8;
    --rule: #4a4a4a;
    --social-blue: #3e7fc1;
  }
  * { margin: 0; padding: 0; box-sizing: border-box; }
  html, body {
    width: 1200px; height: 900px; overflow: hidden;
    background: var(--canvas-bg);
    font-family: "Open Sans", Arial, sans-serif;
  }
  .canvas { position: relative; width: 1200px; height: 900px; }
  .card {
    position: absolute; width: 560px; height: 320px;
    border-radius: 22px; overflow: hidden;
    background: linear-gradient(160deg, var(--card-top), var(--card-bottom));
    box-shadow: 0 12px 30px rgba(0,0,0,.6);
  }
  .card--back { left: 140px; top: 110px; }
  .card--front { left: 500px; top: 470px; }
  .card__decoration {
    position: absolute; left: -40px; top: 20px; width: 300px; height: 300px;
    border-radius: 50%;
    background: radial-gradient(circle at 55% 40%, var(--deco-tone), transparent 70%);
  }
  .brand {
    position: absolute; display: flex; align-items: center; gap: 12px;
    font-weight: 600; color: var(--brand-green); letter-spacing: 1px;
    white-space: nowrap;
  }
  .brand__dot { width: 14px; height: 14px; border-radius: 50%; background: var(--brand-brown); flex: none; }
  .card--back .brand { left: 250px; top: 70px; font-size: 40px; }
  .tagline {
    position: absolute; right: 60px; bottom: 60px;
    color: var(--text-light); font-size: 14px; letter-spacing: .6px;
    text-transform: uppercase; white-space: nowrap;
  }
  .card--front .brand { right: 40px; top: 50px; font-size: 32px; }
  .divider {
    position: absolute; left: 0; right: 40px; top: 120px;
    height: 1px; background: var(--rule);
  }
  .social {
    position: absolute; right: 40px; top: 150px;
    display: flex; align-items: center; gap: 10px;
    color: var(--text-light); font-size: 15px;
  }
  .social__dot { width: 18px; height: 18px; border-radius: 50%; background: var(--social-blue); }
  .person { position: absolute; left: 40px; top: 170px; }
  .person__name {
    font-size: 20px; font-weight: 600; letter-spacing: .5px;
    text-transform: uppercase; padding-bottom: 10px;
    border-bottom: 1px solid var(--rule); width: 260px;
  }
  .person__first { color: var(--brand-brown); }
  .person__last { color: var(--brand-green); }
  .contact { list-style: none; margin-top: 10px; }
  .contact li {
    display: flex; align-items: center; gap: 10px;
    color: var(--text-light); font-size: 15px; line-height: 24px;
  }
  .contact svg { width: 13px; height: 13px; fill: var(--brand-brown); flex: none; }
</style>
</head>
<body>
<main class="canvas">
  <section class="card card--back" aria-label="Card back">
    <div class="card__decoration" role="img" aria-label="Faint background decoration area"></div>
    <div class="brand"><span class="brand__dot"></span>Florivex</div>
    <p class="tagline">Renewal in every single cup</p>
  </section>

  <section class="card card--front" aria-label="Card front">
    <div class="card__decoration" role="img" aria-label="Faint background decoration area"></div>
    <div class="brand"><span class="brand__dot"></span>Florivex</div>
    <div class="divider"></div>
    <div class="social"><span>Florivex</span><span class="social__dot"></span></div>
    <div class="person">
      <h1 class="person__name"><span class="person__first">Peter</span> <span class="person__last">Dalton</span></h1>
      <ul class="contact">
        <li><svg viewBox="0 0 16 16"><path d="M3 1h3l1 4-2 1a9 9 0 0 0 5 5l1-2 4 1v3a2 2 0 0 1-2 2A13 13 0 0 1 1 3a2 2 0 0 1 2-2z"/></svg>0438 216 570</li>
        <li><svg viewBox="0 0 16 16"><path d="M1 3h14v10H1zM2 4l6 5 6-5v-.5H2z"/></svg>info@florivex.com.au</li>
        <li><svg viewBox="0 0 16 16"><circle cx="8" cy="8" r="7"/></svg>www.florivex.com.au</li>
      </ul>
    </div>
  </section>
</main>
</body>
</html>
```